Anzeigengestaltung für Dienstleister für die professionelle Planung und Beschaffung von IT-Lösungen
Zielgruppe
Wir sind Dienstleister für die professionelle Planung und Beschaffung von IT-Lösungen.
Wir bieten umfassende und umfangreiche sowie produktneutrale Beratung zur Umsetzung Ihrer Digitalisierungsprojekte.
Unser Ziel ist es, Ihre individuellen Wünsche und Anforderungen mit speziell auf Sie abgestimmten Konzepten zu realisieren. Hierbei verstehen wir uns als Teamplayer, der alle Aspekte der verschiedenen Fachbereiche zu kombinieren versteht.
Fokus:
Neben den technischen Lösungen erarbeiten wir die detaillierten Anforderungen für Vergabeverfahren (öffentliche Ausschreibung national und EU weit)
Beratung
Planung
Erarbeiten von professionellen und produktneutralen Ausschreibungsunterlagen
Durchführen der Ausschreibung und Vergabe
Professionelle Dokumentation
Professionelle Projektbegleitung bis zur Abnahme und Abrechnung
Bereiche:
Digitalisierung Schulen
Rechenzentren
Telefon Lösungen
Druck Lösungen
Netzwerk und WLAN Lösungen
Zielkunden:
Öffentliche Kunde wie z.B. Kommunen, Schulen, Rathäuser, Hochschulen
Aufgabenstellung
OnePager A4 als Werbeflyer zur Darstellung meines Unternehmen, Neukundengewinnung

```html
<!DOCTYPE html>
<html lang="de">
<head>
<meta charset="utf-8">
<title>Systemkante – Flyer</title>
<link rel="stylesheet" href="https://fonts.googleapis.com/css2?family=Space+Grotesk:wght@400;500;700&display=swap">
<style>
  :root {
    --teal: #66bfac;
    --sky: #94d5ea;
    --sky-deep: #8dd7f0;
    --navy: #1a3d68;
    --navy-dark: #10284a;
    --lime: #b4d334;
    --ink: #111111;
    --slate: #4a5f80;
    --slate-dark: #3e5a7e;
    --white: #ffffff;
  }
  * { margin: 0; padding: 0; box-sizing: border-box; }
  html, body { width: 848px; height: 1200px; overflow: hidden; background: var(--white); }
  body { font-family: "Space Grotesk", Arial, sans-serif; color: var(--ink); }
  .flyer { position: relative; width: 848px; height: 1200px; overflow: hidden; }
  .abs { position: absolute; }

  .corner-block { left: 674px; top: 0; width: 174px; height: 176px; background: var(--teal); }
  .band-top { left: 0; top: 153px; width: 848px; height: 6px; background: var(--sky); }
  .band-mid { left: 273px; top: 698px; width: 575px; height: 6px; background: var(--sky); }
  .side-column { left: 0; top: 695px; width: 94px; height: 505px; background: var(--teal); }

  .brand { left: 58px; top: 44px; display: flex; align-items: center; gap: 12px; }
  .brand-dot { width: 26px; height: 26px; border-radius: 50%; background: var(--lime); }
  .brand-name { font-size: 40px; font-weight: 400; letter-spacing: 2px; color: var(--ink); line-height: 1; }
  .brand-rule { left: 443px; top: 106px; width: 38px; height: 1px; background: var(--lime); }

  .heading { font-size: 20px; font-weight: 700; line-height: 1; }
  .heading-who { left: 161px; top: 116px; }
  .heading-what { left: 106px; top: 520px; }
  .heading-whom { left: 201px; top: 909px; }

  .intro { left: 161px; top: 183px; font-size: 16px; line-height: 20.5px; }
  .intro p + p { margin-top: 20.5px; }

  .hero-visual { left: 374px; top: 280px; width: 474px; height: 311px;
    background: linear-gradient(90deg, var(--sky-deep) 0%, var(--sky-deep) 28%, #4f86b4 48%, var(--navy) 66%, var(--navy-dark) 100%); }
  .data-visual { left: 29px; top: 727px; width: 209px; height: 117px;
    background: linear-gradient(100deg, #1c2f6e 0%, #1f6d8a 45%, #37d1c0 70%, #173a74 100%); }

  .list { list-style: none; font-size: 16px; line-height: 20.5px; }
  .list li { position: relative; }
  .list li::before { content: ""; position: absolute; top: 9px; left: -49px; width: 3px; height: 3px; background: var(--ink); }
  .list-services { left: 108px; top: 560px; }
  .list-areas { left: 324px; top: 731px; }
  .list-clients { left: 201px; top: 944px; }

  .client-box { left: 132px; top: 898px; width: 716px; height: 157px; background: var(--sky); }

  .company { left: 102px; top: 1084px; font-size: 16px; color: var(--slate); line-height: 20.5px; }
  .address { left: 102px; top: 1125px; font-size: 16px; color: var(--slate); line-height: 20.5px; }
  .tagline { left: 328px; top: 1082px; font-size: 20px; color: var(--sky); }
  .contact { left: 556px; top: 1124px; font-size: 19px; color: var(--slate-dark); line-height: 24px; }
  .contact .label { display: inline-block; width: 50px; }
  .contact .label-mail { width: 72px; }
  .contact strong { font-weight: 700; }
</style>
</head>
<body>
<div class="flyer">
  <div class="abs corner-block"></div>
  <div class="abs band-top"></div>
  <div class="abs side-column"></div>
  <div class="abs band-mid"></div>
  <div class="abs client-box"></div>

  <div class="abs brand">
    <span class="brand-dot"></span>
    <span class="brand-name">SYSTEMKANTE</span>
  </div>
  <div class="abs brand-rule"></div>

  <h2 class="abs heading heading-who">Wer wir sind</h2>

  <div class="abs hero-visual" role="img" aria-label="Foto: Person im Hemd tippt auf ein Tablet, darüber leuchtende Diagramme und Kurven"></div>

  <div class="abs intro">
    <p>Wir sind Dienstleister für die professionelle<br>Planung und Beschaffung von IT-Lösungen.</p>
    <p>Wir bieten Ihnen umfassende und umfangrei-<br>che sowie produktneutrale Beratung zur Um-<br>setzung Ihrer Digitalisierungsprojekte.</p>
    <p>Unser Ziel ist es, Ihre individuellen Wünsche<br>und Anforderungen mit speziell auf Sie abge-<br>stimmten Konzepten zu realisieren. Hierbei ver-<br>stehen wir uns als Teamplayer, der alle Aspekte<br>der verschiedenen Fachbereiche zu kombinie-<br>ren versteht. Neben den technischen Lösungen<br>erarbeiten wir die detaillierten Anforderungen<br>für Ihr&nbsp;&nbsp;&nbsp;Vergabeverfahren.</p>
  </div>

  <h2 class="abs heading heading-what">Was wir tun</h2>
  <ul class="abs list list-services">
    <li>Beratung</li>
    <li>Planung</li>
    <li>Erarbeiten von professionellen und produkt neutralen Ausschreibungsunterlagen</li>
    <li>Durchführen der Ausschreibung und Vergabe</li>
    <li>Professionelle Dokumentation</li>
    <li>Professionelle Projektbegleitung bis zur Abnahme und Abrechnung</li>
  </ul>

  <div class="abs data-visual" role="img" aria-label="Abstrakte Datenstrom-Grafik mit leuchtenden Lichtlinien in Türkis und Blau"></div>
  <ul class="abs list list-areas">
    <li>Digitalisierung Schulen</li>
    <li>Rechenzentren</li>
    <li>Telefon Lösungen</li>
    <li>Druck Lösungen</li>
    <li>Netzwerk und WLAN Lösungen</li>
  </ul>

  <h2 class="abs heading heading-whom">Wem wir helfen</h2>
  <ul class="abs list list-clients">
    <li>Öffentliche Kunden wie</li>
    <li>Kommunen</li>
    <li>Schulen</li>
    <li>Rathäuser</li>
    <li>Hochschulen</li>
  </ul>

  <div class="abs company">Systemkante GmbH</div>
  <div class="abs address">Anschrift:<br>Lindenweg 14<br>88400 Musterbach</div>
  <div class="abs tagline">Wir freuen uns auf jede Herausforderung.</div>
  <div class="abs contact">
    <div><span class="label">Tel:</span><strong>07500 / 12345-0</strong></div>
    <div><span class="label label-mail">E-Mail:</span><strong>info@systemkante.de</strong></div>
  </div>
</div>
</body>
</html>
```